Business Card design
Cordavera Ruvek Martial Arts Training Center
I need single sided standard sized Business Card [3.5" x 2"]
Font in logo is CGF Locust Resistance. This font does not need to be used.
Modern
Cordavera Ruvek or Cordavera Ruvek Martial Arts Training Center
Martial Arts Discipline | Athletic Excellence
2671 Bramble Rd
Kalamazoo, MI
info@cordaverix.example
www.cordaverix.example
facebook.com/cordaverix
optional items for the business card:
Pelnor Grappling League
Todd Weslin Jiu Jitsu
Orvane Kickboxing Union
Mixed Martial Arts
Fitness
Can put the logo on one side and the information on the second side if you would like to submit that type of design.
Cordavera Ruvek illustrator file
Cordavera Ruvek eps file

```html
<!DOCTYPE html>
<html lang="en">
<head>
<meta charset="utf-8">
<title>Cordavera Ruvek Stationery</title>
<link href="https://fonts.googleapis.com/css2?family=Open+Sans:wght@400;600;700&display=swap" rel="stylesheet">
<style>
  :root {
    --red: #e1343a;
    --red-dark: #c7262c;
    --grey: #8e8e93;
    --grey-light: #c9c9cc;
    --ink: #4a4a4e;
    --paper: #ffffff;
    --backdrop: #ecebe8;
  }
  * { margin: 0; padding: 0; box-sizing: border-box; }
  html, body { width: 1200px; height: 846px; overflow: hidden; }
  body {
    background: var(--backdrop);
    font-family: "Open Sans", Arial, sans-serif;
    color: var(--ink);
    position: relative;
  }
  .piece {
    position: absolute;
    background: var(--paper);
    overflow: hidden;
    box-shadow: 0 3px 10px rgba(0,0,0,0.18);
  }
  .piece svg.swoosh { position: absolute; left: 0; bottom: 0; width: 100%; }

  .brand {
    display: flex;
    align-items: center;
    gap: 8px;
    font-weight: 700;
    color: var(--red);
    letter-spacing: 0.5px;
    text-transform: uppercase;
    white-space: nowrap;
  }
  .brand .mark { width: 14px; height: 14px; background: var(--red); flex: none; }
  .brand.light { color: var(--paper); }
  .brand.light .mark { background: var(--paper); }

  /* Letterhead */
  .letterhead { left: 252px; top: 72px; width: 564px; height: 708px; }
  .letterhead .brand { position: absolute; left: 36px; top: 36px; font-size: 24px; }
  .letterhead .contact {
    position: absolute; left: 390px; top: 30px;
    font-size: 8.5px; line-height: 1.45; color: var(--grey);
  }
  .contact b { color: var(--red); font-weight: 600; }
  .letterhead .site {
    position: absolute; left: 0; right: 0; bottom: 10px;
    text-align: center; color: var(--paper); font-size: 10px;
  }

  /* Business card front */
  .card-front { left: 48px; top: 192px; width: 408px; height: 192px; border-radius: 14px; }
  .card-front .brand { position: absolute; left: 26px; top: 34px; font-size: 22px; }
  .card-front .address {
    position: absolute; right: 26px; top: 108px;
    font-size: 9px; color: var(--ink);
  }
  .card-front .details {
    position: absolute; left: 0; right: 0; bottom: 14px;
    text-align: center; font-size: 8.5px; color: var(--paper);
  }

  /* Business card back */
  .card-back { left: 48px; top: 396px; width: 408px; height: 187px; border-radius: 14px; }
  .card-back .brand { position: absolute; left: 0; right: 0; top: 70px; justify-content: center; font-size: 20px; }
  .card-back .site {
    position: absolute; left: 0; right: 0; bottom: 22px;
    text-align: center; font-size: 10px; font-weight: 600; color: var(--ink);
  }

  /* Red card */
  .card-red { left: 835px; top: 48px; width: 341px; height: 192px; border-radius: 14px; background: var(--red); }
  .card-red .brand { position: absolute; left: 0; right: 0; top: 76px; justify-content: center; font-size: 20px; }
  .card-red .site {
    position: absolute; left: 0; right: 0; bottom: 22px;
    text-align: center; font-size: 10px; color: var(--paper);
  }

  /* Envelope */
  .envelope { left: 540px; top: 336px; width: 636px; height: 456px; }
  .envelope .flap { position: absolute; left: 0; top: 0; width: 100%; height: 150px; }
  .envelope .flap .brand { position: absolute; left: 0; right: 0; top: 56px; justify-content: center; font-size: 18px; }
  .envelope .brand.main { position: absolute; left: 26px; top: 168px; font-size: 24px; }
  .envelope .contact {
    position: absolute; left: 26px; top: 252px;
    font-size: 8.5px; line-height: 1.45; color: var(--grey);
  }
  .envelope .site {
    position: absolute; left: 0; right: 0; bottom: 14px;
    text-align: center; font-size: 10px; color: var(--paper);
  }
</style>
</head>
<body>

<section class="piece letterhead" aria-label="Letterhead">
  <div class="brand"><span class="mark"></span>Cordavera Ruvek</div>
  <address class="contact" style="font-style:normal">
    2671 Bramble Rd, Kalamazoo, MI 49007<br>
    <b>Phone</b> : 269-555-0148<br>
    <b>Cell</b> : 269-555-0148<br>
    <b>Email</b> : info@cordaverix.example
  </address>
  <svg class="swoosh" viewBox="0 0 564 70" height="70" preserveAspectRatio="none">
    <path d="M0 20 Q280 -8 564 18 L564 34 Q280 6 0 36 Z" fill="var(--grey-light)"/>
    <path d="M0 40 Q280 12 564 38 L564 70 L0 70 Z" fill="var(--red)"/>
  </svg>
  <p class="site">www.cordaverix.example</p>
</section>

<section class="piece card-front" aria-label="Business card, front">
  <div class="brand"><span class="mark"></span>Cordavera Ruvek</div>
  <p class="address">2671 Bramble Rd &nbsp; Kalamazoo, MI 49007</p>
  <svg class="swoosh" viewBox="0 0 408 70" height="70" preserveAspectRatio="none">
    <path d="M0 44 Q200 -6 408 0 L408 16 Q200 10 0 52 Z" fill="var(--grey-light)"/>
    <path d="M0 56 Q200 16 408 20 L408 70 L0 70 Z" fill="var(--red)"/>
  </svg>
  <p class="details">Phone : 269-555-0148 &nbsp; Cell : 269-555-0148 &nbsp; Email : info@cordaverix.example</p>
</section>

<section class="piece card-back" aria-label="Business card, back">
  <div class="brand"><span class="mark"></span>Cordavera Ruvek</div>
  <p class="site">www.cordaverix.example</p>
</section>

<section class="piece card-red" aria-label="Business card, red variant">
  <div class="brand light"><span class="mark"></span>Cordavera Ruvek</div>
  <p class="site">www.cordaverix.example</p>
</section>

<section class="piece envelope" aria-label="Envelope">
  <svg class="flap" viewBox="0 0 636 150" preserveAspectRatio="none">
    <path d="M0 0 L636 0 L636 150 Q318 80 0 150 Z" fill="var(--red)"/>
  </svg>
  <div class="flap"><div class="brand light"><span class="mark"></span>Cordavera Ruvek</div></div>
  <div class="brand main"><span class="mark"></span>Cordavera Ruvek</div>
  <address class="contact" style="font-style:normal">
    2671 Bramble Rd<br>
    Kalamazoo, MI 49007<br>
    <b>Phone</b> : 269-555-0148<br>
    <b>Cell</b> : 269-555-0148<br>
    <b>Email</b> : info@cordaverix.example
  </address>
  <svg class="swoosh" viewBox="0 0 636 80" height="80" preserveAspectRatio="none">
    <path d="M0 22 Q320 -6 636 20 L636 36 Q320 8 0 38 Z" fill="var(--grey-light)"/>
    <path d="M0 42 Q320 14 636 40 L636 80 L0 80 Z" fill="var(--red)"/>
  </svg>
  <p class="site">www.cordaverix.example</p>
</section>

</body>
</html>
```